Grocery store half gallon water carton

We need a 4 sided design for a standard half gallon carton (Larchmont packaging 3.764" x 3.764") you'd see in a grocery store. For the barcode 1.25 W x 1 H inches will be fine for now. I'm assuming we can tweak these things later? I attached a picture of our bulk water machines for further context around the brand. Our product is alkaline water. We want to emphasize our differentials vs. the competition. On the store shelf that will be a cost effective delivery of alkaline water in an eco-friendly container. At a company level it's the statement below. We're open to how to best integrate this neatly and cleanly onto the package.

Our mission is to provide everyone with the highest quality drinking water delivered through the most responsible purification systems that do not damage the environment.

Below are some design considerations from Larchmont packaging

Design Considerations
• Refer to High Definition Flexo Digital File Submission Guidelines.
• Large solids should be used as the 5th color. The reproduction of large background solids by
process inks will not deliver optimum quality.
• When black art needs to be “rich” black, add a 30M-30C-30Y to the 100% black area.
• Thin lines and heavy solid patches in the same color should be avoided, due to flexo
limitations.
• Do not use type styles with combination thick and thin strokes.
• Do not use type styles with fine serifs.
• Do not use condensed type styles.
• Do not use TrueType fonts.
• Embedded fonts must include the font in the file.
• Customers must confirm that a fitment will be used and what size is needed in order to create
the correct design for the gable top package. If there is no fitment, disregard the fitment area
and both gable tops will be identical.
• It is recommended to stay within the panel fold dash lines if copy or art is critical to the fold.
• It is recommended to stay outside the fitment and window dash lines if copy or art is critical
to the die cut.
Updates

Project Deadline Extended Reason: We need to gather more information on fonts, barcodes, and exact specs to provide designers with everything they need. Added Saturday, March 11, 2017

Target Market(s)

Pretty large. Health conscious consumers who already purchase water from the grocery store.

Industry/Entity Type

Grocery Store

Font styles to use
Serif

Requirements
Must have
• Our logo, alkaline water noted, some form of our story told, 4 sides of graphics, space for barcode, space for nutrition facts. Example pictures attached.
Nice to have
• Clean, minimalistic, desirable to put in your cart.
• We're also open to something on the design that emphasizes that we believe in a world without plastic. #sipbeyondbottles, #ditchthejugs ect. Just an idea to float out there.
Should not have
• Too many different colors, too wordy

```html
<!DOCTYPE html>
<html lang="en">
<head>
<meta charset="utf-8">
<title>Lumira Alkaline Water – Half Gallon Carton Panels</title>
<link href="https://fonts.googleapis.com/css2?family=Raleway:wght@400;500;600;700&family=Archivo+Narrow:wght@400;700&display=swap" rel="stylesheet">
<style>
  :root{
    --stage:#9d9c9c;
    --stage-glow:#c9c9c9;
    --paper:#ffffff;
    --aqua:#0ba3cf;
    --navy:#243443;
    --mist:#e9eff1;
    --tide:#4b9ec2;
    --sky:#9fc7d6;
    --warn:#e0323a;
    --ink:#1f2a33;
    --water-word:#c9d6dd;
  }
  *{margin:0;padding:0;box-sizing:border-box;}
  html,body{width:1200px;height:806px;overflow:hidden;}
  body{
    background:radial-gradient(ellipse 260px 420px at 600px 380px,var(--stage-glow),var(--stage) 70%);
    font-family:"Raleway",sans-serif;
    color:var(--ink);
    position:relative;
  }
  .gable{position:absolute;top:120px;width:246px;height:92px;}
  .gable svg{position:absolute;inset:0;}
  .gable-tag{
    position:absolute;left:0;right:0;top:42px;text-align:center;
    font-size:16px;font-weight:500;color:var(--navy);letter-spacing:.2px;
  }
  .panel{
    position:absolute;top:216px;width:246px;height:477px;background:var(--paper);
    overflow:hidden;box-shadow:0 2px 5px rgba(0,0,0,.35);
  }
  .panel > svg.art{position:absolute;inset:0;}
  .p1{left:82px;} .p2{left:346px;} .p3{left:606px;} .p4{left:866px;}
  .g1{left:82px;} .g2{left:346px;} .g3{left:606px;} .g4{left:866px;}

  .free-of{
    position:absolute;left:140px;width:72px;text-align:center;
    font-size:13px;color:var(--navy);letter-spacing:.3px;transform:translateY(-50%);
  }
  .badge{
    position:absolute;border-radius:50%;background:var(--navy);color:var(--paper);
    display:flex;flex-direction:column;align-items:center;justify-content:center;text-align:center;
  }
  .badge-name{font-weight:400;line-height:1;}
  .badge-sub{font-weight:400;letter-spacing:.3px;}
  .badge-fine{font-weight:400;letter-spacing:.2px;}
  .badge-lg{left:48px;top:155px;width:148px;height:148px;}
  .badge-lg .badge-name{font-size:38px;}
  .badge-lg .badge-sub{font-size:11px;margin-top:14px;}
  .badge-lg .badge-fine{font-size:5px;}
  .badge-sm{width:72px;height:72px;}
  .badge-sm .badge-name{font-size:19px;}
  .badge-sm .badge-sub{font-size:5.5px;margin-top:6px;}
  .badge-sm .badge-fine{font-size:3px;}

  .claim{position:absolute;left:134px;top:326px;color:var(--navy);}
  .claim-title{font-size:17px;font-weight:600;letter-spacing:1.6px;line-height:15px;}
  .claim-body{font-size:9.5px;font-weight:500;line-height:13.5px;margin-top:4px;}
  .claim-tag{font-size:8.5px;color:var(--paper);margin-top:8px;}

  .quote-mark{
    position:absolute;left:26px;top:150px;font-size:110px;font-weight:700;
    line-height:1;color:var(--navy);font-family:"Raleway",sans-serif;
  }
  .mission{
    position:absolute;left:27px;top:264px;width:120px;
    font-size:12.4px;font-weight:500;line-height:14.5px;color:var(--navy);
  }

  .water-word{
    position:absolute;left:108px;top:480px;transform-origin:0 0;transform:rotate(-90deg);
    font-size:152px;font-weight:400;line-height:1;letter-spacing:-2px;
    background:linear-gradient(90deg,var(--water-word),#aebfc9 70%,var(--tide));
    -webkit-background-clip:text;background-clip:text;color:transparent;
  }
  .nutrition{
    position:absolute;left:17px;top:221px;width:84px;background:var(--paper);
    border:1px solid var(--ink);padding:2px 2px;font-family:"Archivo Narrow",sans-serif;
    color:var(--ink);font-size:5px;line-height:6.4px;
  }
  .nf-title{font-size:10px;font-weight:700;line-height:10px;}
  .nf-rule{border-top:2.5px solid var(--ink);margin:1px 0;}
  .nf-thin{border-top:.6px solid var(--ink);}
  .nf-row{display:flex;justify-content:space-between;}
  .nf-b{font-weight:700;}
  .nf-note{font-size:3.4px;line-height:4.4px;}
  .ingredients{
    position:absolute;left:17px;top:391px;width:86px;font-family:"Archivo Narrow",sans-serif;
    font-size:6px;line-height:7px;color:var(--ink);
  }
  .ingredients b{font-weight:700;}
</style>
</head>
<body>

<!-- Gable tops -->
<div class="gable g1"><svg viewBox="0 0 246 92" width="246" height="92"><polygon points="0,92 123,0 246,92" fill="#ffffff"/></svg></div>
<div class="gable g2"><svg viewBox="0 0 246 92" width="246" height="92"><polygon points="0,92 22,0 224,0 246,92" fill="#ffffff"/></svg><div class="gable-tag">#sipbeyondbottles</div></div>
<div class="gable g3"><svg viewBox="0 0 246 92" width="246" height="92"><polygon points="0,92 123,0 246,92" fill="#ffffff"/></svg></div>
<div class="gable g4"><svg viewBox="0 0 246 92" width="246" height="92"><polygon points="0,92 22,0 224,0 246,92" fill="#ffffff"/></svg><div class="gable-tag">#sipbeyondbottles</div></div>

<!-- Panel 1: free-of claims -->
<section class="panel p1">
  <svg class="art" viewBox="0 0 246 477" width="246" height="477">
    <path d="M246 0 L246 477 L150 477 C108 448 83 402 83 345 C83 262 168 140 246 0Z" fill="var(--aqua)"/>
    <g fill="none" stroke="var(--warn)" stroke-width="2.2">
      <circle cx="176" cy="238" r="24"/><line x1="159" y1="221" x2="193" y2="255"/>
      <circle cx="176" cy="301" r="24"/><line x1="159" y1="284" x2="193" y2="318"/>
      <circle cx="176" cy="365" r="24"/><line x1="159" y1="348" x2="193" y2="382"/>
    </g>
  </svg>
  <div class="free-of" style="top:238px">LEAD</div>
  <div class="free-of" style="top:301px;left:130px;width:92px">FLOURIDE</div>
  <div class="free-of" style="top:365px;left:130px;width:92px">CHLORINE</div>
</section>

<!-- Panel 2: front -->
<section class="panel p2">
  <svg class="art" viewBox="0 0 246 477" width="246" height="477">
    <defs>
      <linearGradient id="frontDrop" x1="0" y1="0" x2="0" y2="1">
        <stop offset="0" stop-color="#f1f5f6"/><stop offset=".55" stop-color="#a9ccd8"/><stop offset="1" stop-color="#4b9ec2"/>
      </linearGradient>
      <linearGradient id="splash" x1="0" y1="0" x2="0" y2="1">
        <stop offset="0" stop-color="#dfe7eb"/><stop offset=".5" stop-color="#9fb3bd"/><stop offset="1" stop-color="#c6d3d9"/>
      </linearGradient>
    </defs>
    <path d="M0 0 L0 477 L150 477 C138 430 125 390 110 350 C80 260 40 140 0 0Z" fill="var(--aqua)"/>
    <path d="M246 25 C200 110 82 240 82 340 C82 410 112 460 135 477 L246 477Z" fill="url(#frontDrop)"/>
    <rect x="4" y="10" width="150" height="160" rx="60" fill="url(#splash)" opacity=".85" role="img" aria-label="Photo of a splashing water crown rising on a thin water column"/>
    <rect x="68" y="170" width="12" height="300" fill="url(#splash)" role="img" aria-label="Thin column of falling water"/>
  </svg>
  <div class="badge badge-lg">
    <div class="badge-name">Lumira</div>
    <div class="badge-sub">ALKALINE H2O</div>
    <div class="badge-fine">+ ELECTROLYTES for taste</div>
  </div>
  <div class="claim">
    <div class="claim-title">PURIFIED<br>WATER</div>
    <div class="claim-body">for the<br>environmentally<br>responsible</div>
    <div class="claim-tag">#sipbeyondbottles</div>
  </div>
</section>

<!-- Panel 3: mission -->
<section class="panel p3">
  <svg class="art" viewBox="0 0 246 477" width="246" height="477">
    <defs>
      <linearGradient id="missionDrop" x1="0" y1="0" x2="0" y2="1">
        <stop offset="0" stop-color="#ffffff"/><stop offset=".5" stop-color="#cfe0e7"/><stop offset="1" stop-color="#4b9ec2"/>
      </linearGradient>
      <linearGradient id="ripple" x1="0" y1="0" x2="0" y2="1">
        <stop offset="0" stop-color="#ffffff" stop-opacity="0"/><stop offset=".35" stop-color="#c7cfd3"/><stop offset="1" stop-color="#a7b2b8"/>
      </linearGradient>
    </defs>
    <rect x="0" y="300" width="246" height="177" fill="url(#ripple)" role="img" aria-label="Photo of a water droplet landing on a rippling water surface"/>
    <path d="M0 5 C60 110 163 250 163 335 C163 415 118 465 95 477 L0 477Z" fill="url(#missionDrop)"/>
  </svg>
  <div class="badge badge-sm" style="left:143px;top:44px">
    <div class="badge-name">Lumira</div>
    <div class="badge-sub">ALKALINE H2O</div>
    <div class="badge-fine">+ ELECTROLYTES for taste</div>
  </div>
  <div class="quote-mark">“</div>
  <p class="mission">Our mission is to provide everyone with the highest quality drinking water delivered through the most responsible purification systems that do not damage the environment.</p>
</section>

<!-- Panel 4: nutrition -->
<section class="panel p4">
  <svg class="art" viewBox="0 0 246 477" width="246" height="477">
    <defs>
      <linearGradient id="rippleSide" x1="0" y1="0" x2="0" y2="1">
        <stop offset="0" stop-color="#ffffff" stop-opacity="0"/><stop offset=".5" stop-color="#d2d9dc"/><stop offset="1" stop-color="#b9c3c8"/>
      </linearGradient>
    </defs>
    <rect x="0" y="260" width="246" height="217" fill="url(#rippleSide)" role="img" aria-label="Photo of rippling water surface"/>
    <rect x="110" y="0" width="136" height="477" fill="#ffffff" opacity=".55"/>
  </svg>
  <div class="water-word">water</div>
  <div class="badge badge-sm" style="left:22px;top:48px">
    <div class="badge-name">Lumira</div>
    <div class="badge-sub">ALKALINE H2O</div>
    <div class="badge-fine">+ ELECTROLYTES for taste</div>
  </div>
  <div class="nutrition">
    <div class="nf-title">Nutrition Facts</div>
    <div>Serving Size: 8 fl oz (240 mL)</div>
    <div>Servings Per Container: About 6</div>
    <div class="nf-rule"></div>
    <div class="nf-b">Amount Per Serving</div>
    <div class="nf-thin"></div>
    <div><span class="nf-b">Calories</span> 0</div>
    <div class="nf-rule"></div>
    <div style="text-align:right">% Daily Value*</div>
    <div class="nf-thin"></div>
    <div class="nf-row"><span><span class="nf-b">Total Fat</span> 0g</span><span>0%</span></div>
    <div class="nf-thin"></div>
    <div class="nf-row"><span><span class="nf-b">Sodium</span> 0mg</span><span>0%</span></div>
    <div class="nf-thin"></div>
    <div class="nf-row"><span><span class="nf-b">Total Carbohydrate</span> 0g</span><span>0%</span></div>
    <div class="nf-thin"></div>
    <div><span class="nf-b">Protein</span> 0g</div>
    <div class="nf-rule"></div>
    <div class="nf-note">Not a significant source of other nutrients.</div>
    <div class="nf-thin"></div>
    <div class="nf-note">*Percent Daily Values based on a 2,000 calorie diet.</div>
  </div>
  <div class="ingredients"><b>INGREDIENTS:</b> purified water, sodium bicarbonate, dipotassium phosphate, magnesium sulfate and calcium chloride*<br>*electrolytes for taste</div>
</section>

</body>
</html>
```